Zielgruppe
FUNKELHAUS kümmert sich dauerhaft um die Strom- und Gasverträge seiner privaten und gewerblichen Kunden. Konkret heißt das: Wir recherchieren jedes Jahr für den Kunden den günstigsten seriösen Strom/Gaslieferanten und wechseln den Kunden zu diesem Lieferanten. Wir übernehmen dabei sämliche Kommunikation mit Kunden, Lieferanten, Netzbetreibern etc. Der Kunde hat dauerhaft uns als Ansprechparter. Die Dienstleistung ist vergleichbar zu einem Steuerberater: Der Kunde bezahlt uns, damit wir uns um seine Verträge kümmern und für ihn sparen. Die Bezahlung erfolgt auf Provisionsbasis. 30% der durch einen Lieferantenwechsel eingesparten Kosten erhalten wir als Lohn. Das heißt für den Kunden: FUNKELHAUS hat dasselbe Ziel: Möglichst viel sparen, da dann auch das Kuchenstück (die 30%) für FUNKELHAUS größer ist. Außerdem hat der Kunde kein Risiko, denn wenn FUNKELHAUS nichts für ihn sparen kann, zahlt er auch nichts.
Die Zielgruppe des anzufertigenden Flyers sind Eigenheimbesitzer mit einer Gasheizung, d.h. eher ältere Menschen
Aufgabenstellung
Der Flyer (DIN A4) soll eine integrierte Antwortpostkarte enthalten, die ausgefüllt und ausgeschnitten an uns zurückgeschickt werden kann. Über die Postkarte kann dann bei uns ein Angebot angefordert werden.
Auf der Postkarte müssen damit für Strom und/oder Gas verschiedene Felder zur Verfügung stehen (Absendeadresse des Interessenten, Jahresverbrauch, derzeitige Preise, Kontaktmöglichkeiten & Sonderwünsche, etc.).
Da der Flyer über Briefexpress verteilt werden soll, wird auf den Flyer die Kundenadresse aufgedruckt ('An die Bewohner des Hauses....'. Dazu muss ein Feld freigehalten werden. Konkret muss das Layout entsprechend den Vorgaben der Post erstellt werden. Diese sind in einer angehängten .pdf zu finden auf Seite 37 der pdf (bzw. 35 des Dokuments)
Wegen Nachfrage: Der Flyer soll nicht gefaltet werden, er wird tatsächlich als nicht-umhüllte DIN-A4 Karte von der Post verteilt. Dazu muss die Empfängeradresse der Antwortpostkarte (d.h. Adresse von Funkelhaus) auf der Rückseite des Flyer angebracht werden.
Der Flyer soll unserem Corporate Design entsprechen, einiges an Material wird bereit gestellt
Das beigefügte Material muss nicht übernommen werden. Im Gegenteil wünschen wir gerne auch andere Vorschläge!

```html
<!DOCTYPE html>
<html lang="de">
<head>
<meta charset="utf-8">
<title>FUNKELHAUS – Flyer</title>
<link rel="stylesheet" href="https://fonts.googleapis.com/css2?family=Montserrat:wght@400;500;600;700&display=swap">
<style>
  :root {
    --brand-blue: #0b5699;
    --band-blue: #005597;
    --accent-orange: #ef7d00;
    --accent-red: #d0191c;
    --paper: #ffffff;
  }
  * { margin: 0; padding: 0; box-sizing: border-box; }
  html, body { width: 849px; height: 1200px; overflow: hidden; background: var(--paper); }
  body { font-family: "Montserrat", Arial, sans-serif; color: var(--brand-blue); }
  .flyer { position: relative; width: 849px; height: 1200px; overflow: hidden; background: var(--paper); }

  .brand { position: absolute; left: 408px; top: 90px; display: flex; align-items: center; gap: 12px; z-index: 2; }
  .brand-dot { width: 30px; height: 30px; border-radius: 50%; background: var(--accent-orange); }
  .brand-name { font-size: 44px; line-height: 1; font-weight: 500; letter-spacing: 1px; color: var(--brand-blue); }

  .recipient { position: absolute; left: 81px; top: 203px; font-size: 12px; font-weight: 500; letter-spacing: 0.2px; z-index: 2; }

  .hero-art { position: absolute; left: 455px; top: 170px; width: 394px; height: 622px; z-index: 1;
    background: linear-gradient(160deg, #eef3f9 0%, #dbe6f2 70%, #f4e1e1 100%); border-radius: 40px 0 0 0; }

  .headline { position: absolute; left: 34px; top: 290px; font-size: 44px; line-height: 41px; font-weight: 400; letter-spacing: 0.5px; z-index: 2; white-space: nowrap; }

  .intro { position: absolute; left: 35px; top: 432px; width: 400px; font-size: 16px; line-height: 21.4px; font-weight: 400; z-index: 2; white-space: nowrap; }

  .reply-band { position: absolute; left: 0; top: 801px; width: 849px; height: 399px; background: var(--band-blue); color: var(--paper); }
  .cut-line { position: absolute; left: 0; top: 800px; width: 849px; border-top: 1.5px dashed #ffffff; z-index: 3; }
  .scissors { position: absolute; left: 6px; top: 785px; z-index: 3; }

  .steps-title { position: absolute; left: 29px; top: 52px; font-size: 36px; font-weight: 400; letter-spacing: 1px; }

  .step-circle { position: absolute; width: 90px; height: 90px; border-radius: 50%; background: var(--accent-orange);
    display: flex; align-items: center; justify-content: center; }
  .step-number { position: absolute; font-size: 34px; font-weight: 400; line-height: 1; }

  .step-text { position: absolute; width: 210px; text-align: center; }
  .step-heading { font-size: 15px; line-height: 17px; font-weight: 600; letter-spacing: 0.3px; }
  .step-desc { margin-top: 4px; font-size: 8.6px; line-height: 11.3px; font-weight: 400; }
  .step-desc b { font-weight: 700; }

  .loop-label { position: absolute; left: 519px; top: 191px; width: 120px; text-align: center; font-size: 15px; line-height: 17px; font-weight: 600; }
  .flow-arrows { position: absolute; left: 0; top: 0; }
</style>
</head>
<body>
<main class="flyer">
  <header class="brand">
    <span class="brand-dot"></span>
    <span class="brand-name">FUNKELHAUS</span>
  </header>

  <p class="recipient">AN DIE BEWOHNER DES HAUSES</p>

  <div class="hero-art" role="img" aria-label="Illustration eines erschöpften Mannes mit roter Krawatte am Schreibtisch, vor ihm Vertragsunterlagen"></div>

  <h1 class="headline">ÜBERFORDERT IM<br>DSCHUNGEL DER<br>STROMANBIETER?</h1>

  <p class="intro">FUNKELHAUS recherchiert jedes Jahr<br>für den Kunden den günstigsten seriö-<br>sen Strom/Gaslieferanten und wechselt<br>den Kunden zu diesem Lieferanten. Wir<br>übernehmen dabei sämliche Kommu-<br>nikation mit Kunden, Lieferanten, Netz-<br>betreibern etc. Sie haben dauerhaft uns<br>als Ansprechparter. Die Dienstleistung<br>ist vergleichbar zu einem Steuerberater:<br>Der Kunde bezahlt uns, damit wir uns<br>um seine Verträge kümmern und für<br>ihn sparen. Sie haben kein Risiko, denn<br>wenn FUNKELHAUS nichts für Sie<br>sparen kann, zahlen Sie auch nichts!</p>

  <section class="reply-band">
    <h2 class="steps-title">SO EINFACH GEHT‘S:</h2>

    <svg class="flow-arrows" width="849" height="399" viewBox="0 0 849 399" aria-hidden="true">
      <defs>
        <linearGradient id="fade-right" gradientUnits="userSpaceOnUse" x1="200" y1="0" x2="316" y2="0"><stop offset="0" stop-color="#fff" stop-opacity="0"/><stop offset="0.4" stop-color="#fff"/></linearGradient>
        <linearGradient id="fade-left" gradientUnits="userSpaceOnUse" x1="620" y1="0" x2="470" y2="0"><stop offset="0" stop-color="#fff" stop-opacity="0"/><stop offset="0.4" stop-color="#fff"/></linearGradient>
      </defs>
      <g fill="none" stroke-width="4" stroke-linecap="round">
        <line x1="200" y1="247" x2="314" y2="247" stroke="url(#fade-right)"/>
        <polyline points="304,237 316,247 304,257" stroke="#fff"/>
        <line x1="620" y1="247" x2="472" y2="247" stroke="url(#fade-left)"/>
        <polyline points="482,237 470,247 482,257" stroke="#fff"/>
        <line x1="518" y1="126" x2="446" y2="205" stroke="#fff" opacity="0.9"/>
        <polyline points="444,191 442,209 460,206" stroke="#fff"/>
        <line x1="611" y1="132" x2="684" y2="205" stroke="#fff" opacity="0.9"/>
        <polyline points="670,208 688,209 686,191" stroke="#fff"/>
      </g>
    </svg>

    <span class="step-number" style="left:60px; top:233px;">1</span>
    <div class="step-circle" style="left:83px; top:202px;">
      <svg width="44" height="52" viewBox="0 0 44 52" aria-hidden="true"><path d="M14 4a5 5 0 0 1 10 0v18h4a4 4 0 0 1 4 2h2a4 4 0 0 1 4 3h1a4 4 0 0 1 4 4v9c0 7-5 12-12 12H21c-4 0-7-2-9-5L4 33a4 4 0 0 1 6-5l4 4z" fill="#fff"/></svg>
    </div>
    <div class="step-text" style="left:23px; top:307px;">
      <div class="step-heading">TARIF-CHECK<br>ANFORDERN</div>
      <div class="step-desc">Fordern Sie <b>kostenlos und unverbindlich</b><br>ein angebot für die senkung ihrer<br>strom- und /oder Gaskosten</div>
    </div>

    <span class="step-number" style="left:334px; top:233px;">2</span>
    <div class="step-circle" style="left:364px; top:202px;">
      <svg width="60" height="50" viewBox="0 0 60 50" aria-hidden="true"><g fill="#fff" stroke="#fff" stroke-width="3"><line x1="30" y1="4" x2="30" y2="42"/><line x1="8" y1="10" x2="52" y2="10"/><line x1="8" y1="10" x2="2" y2="28"/><line x1="8" y1="10" x2="14" y2="28"/><line x1="52" y1="10" x2="46" y2="28"/><line x1="52" y1="10" x2="58" y2="28"/><path d="M1 28h14a7 7 0 0 1-14 0zM45 28h14a7 7 0 0 1-14 0z" stroke="none"/><rect x="18" y="42" width="24" height="5" stroke="none"/></g></svg>
    </div>
    <div class="step-text" style="left:309px; top:307px;">
      <div class="step-heading">BEST-TARIF<br>CHECK</div>
      <div class="step-desc">Wir prüfen objektiv <b>alle seriösen Anbieter</b><br>Ihrer Region und ermitteln den für Sie<br>günstigsten Strom- und/oder Gas-Tarif</div>
    </div>

    <span class="step-number" style="left:491px; top:73px;">3</span>
    <div class="step-circle" style="left:519px; top:42px;">
      <svg width="50" height="40" viewBox="0 0 50 40" aria-hidden="true"><circle cx="33" cy="9" r="7" fill="#fff"/><ellipse cx="23" cy="24" rx="18" ry="12" fill="#fff"/><rect x="10" y="30" width="6" height="9" fill="#fff"/><rect x="28" y="30" width="6" height="9" fill="#fff"/><rect x="2" y="20" width="5" height="7" fill="#fff"/></svg>
    </div>
    <div class="step-text" style="left:608px; top:40px;">
      <div class="step-heading">BEST-TARIF<br>WECHSEL</div>
      <div class="step-desc">Wenn Sie einverstanden sind, überneh-<br>men wür für Sie den sicheren Wechsel<br>zum günstigsten seriösen Anbieter von<br>Gas und/oder Strom. Unsere Vergütung<br>beträgt <b>30 % der Kostenersparnis</b>.</div>
    </div>

    <span class="step-number" style="left:644px; top:233px;">4</span>
    <div class="step-circle" style="left:675px; top:202px;">
      <svg width="54" height="44" viewBox="0 0 54 44" aria-hidden="true"><g fill="none" stroke="#fff" stroke-width="6"><path d="M8 22a19 19 0 0 1 34-10"/><path d="M46 22a19 19 0 0 1-34 10"/></g><path d="M36 4l12 8-14 4z" fill="#fff"/><path d="M18 40L6 32l14-4z" fill="#fff"/></svg>
    </div>
    <div class="step-text" style="left:601px; top:307px; width:240px;">
      <div class="step-heading">BEST-CHECK<br>AUTOMATIK</div>
      <div class="step-desc">Wir behalten Ihre Tarife im Blick und sorgen<br>dafür, dass Sie Strom und/or Gas <b>daurhaft vom</b><br><b>günstigsten seriösen Anbieter</b> beziehen.</div>
    </div>

    <div class="loop-label">DAUERHAFT<br>SPAREN</div>
  </section>

  <div class="cut-line"></div>
  <svg class="scissors" width="40" height="32" viewBox="0 0 40 32" aria-hidden="true">
    <g fill="none" stroke="#ef7d00" stroke-width="2.5"><circle cx="6" cy="6" r="4"/><circle cx="6" cy="26" r="4"/><line x1="9" y1="9" x2="38" y2="24"/><line x1="9" y1="23" x2="38" y2="8"/></g>
  </svg>
</main>
</body>
</html>
```